Establishing a website for a non profit organisation

The foundation is called:

German: Edle Alte Bruderschaft des Hofes Lindenmark e.V.

Englisch (Translation): Noble old Brotherhood of Court Lindenmark e.V.

The foundation is a legal nonprofit organization with the purpose to help people in need. The foundation - a charitable organization - donates funds and supports solely and directly people living in Frankfurt and in Germany.

In some cases the foundation works together with other charitable organizations that support projects to help people in need.

The foundation also functions as trustee with powers of administration of property in trust with a legal obligation to administer it solely for the purposes specified. The purpose is not to generate/obtain wealth for shareholders but to respectfully execute the benevolent intentions of the founders/testators in the interest of the legatee.

The foundation was established in 1408.

The website should give a good and easy overview about the foundation work.
It should be easy to figure out how to participate and help the organisation.
Either you can participate with a one time donation, with a regular donation or with a testament.

For those with donation it is possible to hand over an contribution receipt for tax purposes.

The main color should be red: RGB R:229 - G:47 - B:34

```html
<!DOCTYPE html>
<html lang="en">
<head>
<meta charset="utf-8">
<title>EABHL e.V – Noble old Brotherhood of Court Lindenmark e.V.</title>
<link rel="stylesheet" href="https://fonts.googleapis.com/css2?family=Arimo:wght@400;700&display=swap">
<style>
:root{
  --red:#e52f22;
  --red-dark:#c9271b;
  --ink:#3a3a3a;
  --body:#555555;
  --grey-band:#3d3d3d;
  --footer:#585858;
  --footer-text:#d6d6d6;
  --tick:#7cb82f;
  --white:#ffffff;
}
*{margin:0;padding:0;box-sizing:border-box}
html,body{width:1086px;height:1200px;overflow:hidden;background:var(--white)}
body{font-family:"Arimo",Arial,sans-serif;color:var(--body);position:relative}
.abs{position:absolute}

.topbar{left:0;top:0;width:1086px;height:36px;background:var(--red);color:var(--white);font-size:9.6px}
.topbar .contact{left:158px;top:13px;display:flex;gap:18px;align-items:center}
.topbar .contact span{display:flex;align-items:center;gap:6px}
.topbar .follow{right:155px;top:13px;display:flex;gap:14px;align-items:center}
.social-dot{width:11px;height:11px;border:1.5px solid var(--white);border-radius:50%;display:inline-block}

.brand{left:155px;top:54px;display:flex;align-items:center;gap:8px}
.brand-mark{width:44px;height:44px;border-radius:50%;background:#8f8f8f}
.brand-name{font-size:23px;font-weight:700;color:var(--red);letter-spacing:.5px}

.nav{top:76px;left:384px;width:548px;display:flex;justify-content:space-between;font-size:11.5px;color:var(--ink)}

.hero{left:156px;top:114px;width:776px;height:308px;
  background:linear-gradient(180deg,#8a8f91 0%,#a7abab 30%,#6b6a63 52%,#7a6f60 68%,#8c8370 100%)}
.slide-arrow{top:146px;width:36px;height:36px;background:rgba(229,47,34,.55);display:flex;align-items:center;justify-content:center}
.slide-arrow.prev{left:0}
.slide-arrow.next{right:0}

.band{left:156px;top:422px;width:776px;height:89px;background:var(--grey-band)}
.band h2{position:absolute;left:25px;top:22px;font-size:15px;font-weight:700;color:var(--white);letter-spacing:.2px}
.band p{position:absolute;left:26px;top:50px;font-size:13.5px;color:#dcdcdc}
.btn{background:var(--red);color:var(--white);font-weight:400;display:flex;align-items:center;justify-content:center;border-bottom:3px solid var(--red-dark);border-radius:2px}
.band .btn{position:absolute;left:590px;top:24px;width:164px;height:40px;font-size:13.5px}

.intro{left:156px;top:538px;width:776px;font-size:12.8px;line-height:25px;color:var(--ink)}

.section-title{font-size:16px;font-weight:700;color:var(--red)}
.small{font-size:9.4px;line-height:18px;color:var(--ink)}

.welcome{left:156px;top:618px;width:340px}
.welcome .small{margin-top:11px}
.ticks{list-style:none;margin-top:9px}
.ticks li{display:flex;align-items:center;gap:8px;height:28px;font-size:10.2px;color:var(--ink)}

.about{left:567px;top:618px;width:340px}
.about .small{margin-top:11px}
.about .small+.small{margin-top:18px}
.about .btn{width:108px;height:33px;font-size:11.5px;margin-top:18px}

.service{top:886px;width:176px}
.service h3{font-size:14.5px;font-weight:400;color:var(--red);margin-bottom:6px}
.service .photo{width:176px;height:110px}
.service .small{margin-top:12px;font-size:9.4px}

.footer{left:0;top:1138px;width:1086px;height:62px;background:var(--footer);color:var(--footer-text);font-size:9.6px}
.footer .links{left:157px;top:26px;display:flex;gap:15px}
.footer .copy{left:739px;top:26px}
</style>
</head>
<body>

<header class="abs topbar">
  <div class="abs contact">
    <span><svg width="7" height="11" viewBox="0 0 7 11"><rect x=".75" y=".75" width="5.5" height="9.5" rx="1" fill="none" stroke="#fff" stroke-width="1.2"/><circle cx="3.5" cy="8.5" r=".7" fill="#fff"/></svg>Call Us : ( 1207 ) 415 608</span>
    <span><svg width="12" height="9" viewBox="0 0 12 9"><rect width="12" height="9" fill="#fff"/><path d="M0 0 6 5 12 0" fill="none" stroke="#e52f22" stroke-width="1.2"/></svg>Email Us : eabhl@mail-post.org</span>
  </div>
  <div class="abs follow">
    <span>Follow Us :</span>
    <span class="social-dot" role="img" aria-label="Social network link"></span>
    <span class="social-dot" role="img" aria-label="Social network link"></span>
    <span class="social-dot" role="img" aria-label="Social network link"></span>
    <span class="social-dot" role="img" aria-label="Social network link"></span>
    <span class="social-dot" role="img" aria-label="News feed link"></span>
  </div>
</header>

<div class="abs brand">
  <span class="brand-mark"></span>
  <span class="brand-name">EABHL e.V</span>
</div>

<nav class="abs nav">
  <span>Home</span><span>About us</span><span>Services</span><span>Donate</span><span>Testimonials</span><span>Contact us</span>
</nav>

<section class="abs hero" role="img" aria-label="City skyline with domed cathedral and river under a cloudy sky">
  <div class="abs slide-arrow prev"><svg width="10" height="16" viewBox="0 0 10 16"><path d="M8 1 2 8l6 7" fill="none" stroke="#fff" stroke-width="1.5"/></svg></div>
  <div class="abs slide-arrow next"><svg width="10" height="16" viewBox="0 0 10 16"><path d="M2 1l6 7-6 7" fill="none" stroke="#fff" stroke-width="1.5"/></svg></div>
</section>

<section class="abs band">
  <h2>DONATION YOU MAKE ARE EXEMPTED FROM TAX</h2>
  <p>We are a legal nonprofit organization with the purpose to help people in need.</p>
  <a class="btn">DONATE HERE</a>
</section>

<p class="abs intro">We are a legal nonprofit organization with the purpose to help people in need. We are a&nbsp; a charitable organization. We donates funds and supports solely and directly people living in Frankfurt and in Germany.</p>

<section class="abs welcome">
  <h2 class="section-title">Welcome to EABHL e.V</h2>
  <p class="small">Lorem Ipsum is simply dummy text of the printing and typesetting industry. Lorem Ipsum has been the industry's standard dummy text ever since the 1500s, when an unknown printer took a galley of type and scrambled it to make a type specimen book.</p>
  <ul class="ticks">
    <li><svg width="13" height="11" viewBox="0 0 13 11"><path d="M1 6l4 4L12 1" fill="none" stroke="#7cb82f" stroke-width="2"/></svg>Lorem Ipsum is simply dummy text of the printing.</li>
    <li><svg width="13" height="11" viewBox="0 0 13 11"><path d="M1 6l4 4L12 1" fill="none" stroke="#7cb82f" stroke-width="2"/></svg>Lorem Ipsum is simply dummy text</li>
    <li><svg width="13" height="11" viewBox="0 0 13 11"><path d="M1 6l4 4L12 1" fill="none" stroke="#7cb82f" stroke-width="2"/></svg>Lorem Ipsum is simply dummy text of the printing.</li>
    <li><svg width="13" height="11" viewBox="0 0 13 11"><path d="M1 6l4 4L12 1" fill="none" stroke="#7cb82f" stroke-width="2"/></svg>Lorem Ipsum is simply dummy text of the printing dummy text.</li>
  </ul>
</section>

<section class="abs about">
  <h2 class="section-title">About Us</h2>
  <p class="small">Lorem Ipsum is simply dummy text of the printing and typesetting industry. Lorem Ipsum has been the industry's standard dummy text ever since the 1500s, when an unknown printer took a galley of type and scrambled.</p>
  <p class="small">Lorem Ipsum is simply dummy text of the printing and typesetting industry. Lorem Ipsum has been the industry's standard dummy text ever since the 1500s, when an unknown printer took a galley of type and scrambled it to make a type specimen book.</p>
  <a class="btn">READ MORE</a>
</section>

<article class="abs service" style="left:156px">
  <h3>Services 01</h3>
  <div class="photo" role="img" aria-label="Hands holding soil with a young green plant" style="background:linear-gradient(135deg,#5a6f9e,#2b3a63)"></div>
  <p class="small">Lorem Ipsum is simply dummy text of the printing and typesetting industry. Lorem Ipsum has been the industry's...</p>
</article>
<article class="abs service" style="left:355px">
  <h3>Services 02</h3>
  <div class="photo" role="img" aria-label="Two hands reaching toward each other against an orange sunset sky" style="background:linear-gradient(135deg,#f2a03a,#c9581c 60%,#7a3a20)"></div>
  <p class="small">Lorem Ipsum is simply dummy text of the printing and typesetting industry. Lorem Ipsum has been the industry's...</p>
</article>
<article class="abs service" style="left:556px">
  <h3>Services 03</h3>
  <div class="photo" role="img" aria-label="Cupped hands holding a paper cut-out family" style="background:radial-gradient(circle at 50% 60%,#b89a86,#1a1412 70%)"></div>
  <p class="small">Lorem Ipsum is simply dummy text of the printing and typesetting industry. Lorem Ipsum has been the industry's...</p>
</article>
<article class="abs service" style="left:756px">
  <h3>Services 04</h3>
  <div class="photo" role="img" aria-label="Portrait of a young child" style="background:linear-gradient(135deg,#6e5a48,#c8a98e 55%,#4a3a2e)"></div>
  <p class="small">Lorem Ipsum is simply dummy text of the printing and typesetting industry. Lorem Ipsum has been the industry's...</p>
</article>

<footer class="abs footer">
  <div class="abs links">
    <span>Home</span><span>|</span><span>About us</span><span>|</span><span>Services</span><span>|</span><span>Donate</span><span>|</span><span>Testimonials</span><span>|</span><span>Contact us</span>
  </div>
  <div class="abs copy">Copyright © 2014. EABHL. All rights reserved.</div>
</footer>

</body>
</html>
```